Men's and Boys sports themed barbershop. I was wanting to see what a black card would look like. I think white is too plain, but I am just needing some ideas for a design or background.

Contact Information for Business Card

Ace Trims
4826 E. Harbor Pine Rd
Pelican Cove, Fl 34512
(352) 555-0142
ace_trims@quellmail.com
Denise Marlow (on one side) Gregory Marlow (on opposite side)
Owner
(555) 555-0187 (Denise) (555) 555-0163

```html
<!DOCTYPE html>
<html lang="en">
<head>
<meta charset="utf-8">
<title>Ace Trims – Business Card</title>
<link rel="stylesheet" href="https://fonts.googleapis.com/css2?family=PT+Sans:wght@400;700&display=swap">
<style>
  :root {
    --backdrop: #e7e4df;
    --card-top: #1d1d1f;
    --card-bottom: #050505;
    --stripe-red: #e3262d;
    --stripe-blue: #3f58a8;
    --stripe-white: #e9e9e9;
    --brand-blue: #3d51a3;
    --text-white: #f2f2f2;
    --contact-blue: #4a5fb4;
    --divider-red: #d8232a;
  }
  html, body {
    margin: 0;
    width: 1200px;
    height: 1200px;
    overflow: hidden;
    background: var(--backdrop);
    font-family: "PT Sans", Arial, sans-serif;
  }
  .sheet { position: relative; width: 1200px; height: 1200px; }
  .card {
    position: absolute;
    left: 150px;
    width: 900px;
    height: 514px;
    background: linear-gradient(160deg, var(--card-top) 0%, var(--card-bottom) 60%);
    box-shadow: 0 10px 28px rgba(0,0,0,0.28);
    overflow: hidden;
  }
  .card--front { top: 56px; }
  .card--back  { top: 630px; }
  .stripes { position: absolute; inset: 0; width: 900px; height: 514px; }
  .stripe { stroke-width: 15; stroke-linecap: butt; }
  .stripe--red   { stroke: var(--stripe-red); }
  .stripe--blue  { stroke: var(--stripe-blue); }
  .stripe--white { stroke: var(--stripe-white); }

  .brand { position: absolute; text-align: center; }
  .card--front .brand { left: 0; right: 0; top: 170px; }
  .card--back  .brand { left: 80px; width: 520px; top: 70px; }
  .brand__name {
    display: block;
    font-weight: 700;
    font-size: 88px;
    line-height: 1;
    color: var(--brand-blue);
    letter-spacing: 1px;
  }
  .card--back .brand__name { font-size: 80px; }
  .tagline {
    display: block;
    margin-top: 18px;
    font-size: 28px;
    letter-spacing: 4px;
    color: var(--text-white);
  }
  .contact {
    position: absolute;
    left: 40px;
    right: 40px;
    top: 320px;
    text-align: center;
    font-style: normal;
    font-size: 26px;
    line-height: 1.35;
    color: var(--contact-blue);
  }
  .contact__name { color: var(--text-white); }
  .contact__divider { color: var(--divider-red); padding: 0 6px; }
</style>
</head>
<body>
<main class="sheet">

  <section class="card card--front" aria-label="Card front">
    <svg class="stripes" viewBox="0 0 900 514" aria-hidden="true">
      <line class="stripe stripe--red"   x1="62"  y1="-4" x2="-2" y2="118"/>
      <line class="stripe stripe--blue"  x1="142" y1="-4" x2="-2" y2="270"/>
      <line class="stripe stripe--white" x1="228" y1="-4" x2="-2" y2="432"/>
      <line class="stripe stripe--red"   x1="720" y1="518" x2="902" y2="172"/>
      <line class="stripe stripe--blue"  x1="800" y1="518" x2="902" y2="324"/>
      <line class="stripe stripe--white" x1="862" y1="518" x2="902" y2="442"/>
    </svg>
    <div class="brand">
      <span class="brand__name">Ace Trims</span>
      <span class="tagline">Sharp Cuts, Every Season</span>
    </div>
  </section>

  <section class="card card--back" aria-label="Card back">
    <svg class="stripes" viewBox="0 0 900 514" aria-hidden="true">
      <line class="stripe stripe--white" x1="598" y1="-4" x2="904" y2="424"/>
      <line class="stripe stripe--blue"  x1="700" y1="-4" x2="904" y2="282"/>
      <line class="stripe stripe--red"   x1="792" y1="-4" x2="904" y2="152"/>
    </svg>
    <div class="brand">
      <span class="brand__name">Ace Trims</span>
      <span class="tagline">Sharp Cuts, Every Season</span>
    </div>
    <address class="contact">
      <div>
        <span class="contact__name">Gregory Marlow</span> (555) 555-0187
        <span class="contact__divider">|</span>
        <span class="contact__name">Denise Marlow</span> (555) 555-0163
      </div>
      <div>ace_trims@quellmail.com</div>
      <div>4826 E. Harbor Pine Rd Pelican Cove</div>
    </address>
  </section>

</main>
</body>
</html>
```